Brindle Works Ltd

I'd like to create a company letterhead for the attached logo in word format.

I'd like to emphasis the icon in large translucent state from the left corner and ensure that the letterhead colouring matches the colour palette of the current logo with a contrast so it's clear to see. I've attached a copy of our sister company page on the app for reference.

```html
<!DOCTYPE html>
<html lang="en">
<head>
<meta charset="utf-8">
<title>Brindle Works Ltd — Letterhead</title>
<link href="https://fonts.googleapis.com/css2?family=Arimo:wght@400&family=Catamaran:wght@600;700&family=Montserrat:wght@400&family=Hind:wght@300&display=swap" rel="stylesheet">
<style>
  :root {
    --teal: #02bfa7;
    --band-grey: #9a9a9a;
    --ink: #555555;
    --paper: #ffffff;
    --backdrop: #dcdcdc;
  }
  * { box-sizing: border-box; margin: 0; padding: 0; }
  html, body {
    width: 1200px; height: 1200px; overflow: hidden;
    background: var(--backdrop);
  }
  .letterhead {
    position: absolute; left: 204px; top: 40px;
    width: 792px; height: 1120px;
    background: var(--paper);
    color: var(--ink);
  }
  .brand {
    position: absolute; top: 62px; left: 0; width: 100%;
    display: flex; justify-content: center; align-items: center; gap: 12px;
  }
  .brand-dot {
    width: 44px; height: 44px; border-radius: 50%;
    background: var(--teal);
  }
  .brand-name {
    font-family: "Montserrat", sans-serif; font-weight: 400;
    font-size: 30px; color: var(--teal); letter-spacing: 0.5px;
  }
  .salutation {
    position: absolute; left: 72px; top: 340px;
    font-family: "Catamaran", sans-serif; font-weight: 700;
    font-size: 19px;
  }
  .letter-body {
    position: absolute; left: 70px; top: 396px; width: 650px;
    font-family: "Arimo", sans-serif; font-size: 13px; line-height: 16.3px;
  }
  .letter-body p { margin-bottom: 14px; }
  .closing {
    position: absolute; left: 72px; top: 730px;
    font-family: "Catamaran", sans-serif; font-weight: 700; font-size: 10.5px;
  }
  .signatory {
    position: absolute; left: 91px; top: 782px;
    font-family: "Hind", sans-serif; font-weight: 300;
    font-size: 20px; letter-spacing: -1px;
  }
  .footer-band {
    position: absolute; left: 0; top: 1028px; width: 100%; height: 72px;
    background: var(--band-grey);
  }
  .footer-contact {
    position: absolute; left: 0; top: 0; width: 365px; height: 72px;
    background: var(--teal); color: var(--paper);
    font-family: "Arimo", sans-serif; font-size: 12.5px;
    padding: 10px 0 0 70px;
  }
  .contact-line { display: flex; align-items: center; gap: 7px; height: 18px; }
  .contact-line svg { width: 11px; height: 11px; fill: var(--paper); }
  .footer-mark {
    position: absolute; left: 348px; top: -10px;
    width: 94px; height: 94px; border-radius: 50%;
    background: var(--paper);
  }
  .footer-address {
    position: absolute; right: 72px; top: 10px;
    text-align: right; color: var(--paper);
    font-family: "Arimo", sans-serif; font-size: 12.5px; line-height: 18px;
  }
</style>
</head>
<body>
<main class="letterhead">
  <header class="brand">
    <span class="brand-dot"></span>
    <span class="brand-name">Brindle Works Ltd</span>
  </header>

  <h1 class="salutation">Dear Mr. Harlan,</h1>

  <section class="letter-body">
    <p>Lorem ipsum dolor sit amet, consectetuer adipiscing elit, sed diam nonmmy nibh euismod tincidunt ut laor eet dolore magna aliquam erat volutpat. Ut wisi enim ad minim veniam, quis nostrud exerci tationmcorper suscipit lobortis nisl ut aliquip ex ea commodo consequat. Duis autem vel eum iriure dolor in hendrerit in vulputate velit esse molestie consequat, vel illum dolore eu feugiat</p>
    <p>Rorem ipsum dolor sit amet, consectetuer adipiscing elit, sed diam nonmmy nibh euismod tincidunt ut laor eet dolore magna aliquam erat volutpat. Ut wisi enim ad minim veniam, quis nostrud exerci tationmcorper suscipit lobortis nisl ut aliquip ex ea commodo consequat. Duis autem vel eum iriure dolor in hendrerit in vulputate velit esse molest</p>
    <p>Dorem ipsum dolor sit amet, consectetuer adipiscing elit, sed diam nonmmy nibh euismod tincidunt ut laor eet dolore magna aliquam erat volutpat. Ut wisi enim ad minim veniam, quis nostrud exerci tationmcorper suscipit lobortis nisl ut aliquip ex ea commodo consequat. Duis autem vel eum iriure dolor in hendrerit in suscipit lobortis nisl ut aliquip ex ea commodo consequat. Duis autem vel eum iriure dolor in hendrerit in vulputate velit esse molestie consequat, vel illum</p>
    <p>Sorem ipsum dolor sit amet, consectetuer adipiscing elit, sed diam nonmmy nibh euismod tincidunt ut laor eet dolore magna aliquam erat volutpat. Ut wisi enim ad minim veniam, quis nostrud exerci tationmcorper suscipit lobortis nisl ut aliquip ex ea commodo consequat. Duis autem vel eum iriure dolor in</p>
  </section>

  <p class="closing">Sincerely,</p>
  <p class="signatory">Dana Whitlow</p>

  <footer class="footer-band">
    <div class="footer-contact">
      <div class="contact-line">
        <svg viewBox="0 0 24 24"><path d="M6.6 10.8a15.1 15.1 0 0 0 6.6 6.6l2.2-2.2a1 1 0 0 1 1-.25 11.4 11.4 0 0 0 3.6.57 1 1 0 0 1 1 1V20a1 1 0 0 1-1 1A17 17 0 0 1 3 4a1 1 0 0 1 1-1h3.5a1 1 0 0 1 1 1c0 1.25.2 2.45.57 3.57a1 1 0 0 1-.25 1z"/></svg>
        <span>123-456-2100</span>
      </div>
      <div class="contact-line">
        <svg viewBox="0 0 24 24"><path d="M2 5h20v14H2z M3 6l9 7 9-7" fill="none" stroke="#fff" stroke-width="2"/></svg>
        <span>office@brindleworks.example</span>
      </div>
      <div class="contact-line">
        <svg viewBox="0 0 24 24"><circle cx="12" cy="12" r="9" fill="none" stroke="#fff" stroke-width="2"/><path d="M3 12h18M12 3c3 3 3 15 0 18M12 3c-3 3-3 15 0 18" fill="none" stroke="#fff" stroke-width="1.6"/></svg>
        <span>www.brindleworks.example</span>
      </div>
    </div>
    <div class="footer-mark"></div>
    <address class="footer-address" style="font-style:normal">
      Your address<br>city<br>state, ZIP 0000
    </address>
  </footer>
</main>
</body>
</html>
```